Bright Fern Painting needs a new business card. See attachments for our logo and current card as an example.
We want to utilize the same colors in the logo, and keep all the information that is currently on it. Just need an updated and modern design.
We are open to loosing the Association Logos if it means a better design.
We are also entertaining a spot for a picture of a headshot of the person listed on the card. Head shot can be finished later.

```html
<!DOCTYPE html>
<html lang="en">
<head>
<meta charset="utf-8">
<title>Bright Fern Painting – Business Card</title>
<link href="https://fonts.googleapis.com/css2?family=Tinos:wght@400;700&display=swap" rel="stylesheet">
<style>
  :root {
    --ink: #000000;
    --paper: #ffffff;
    --serif: "Tinos", "Times New Roman", serif;
  }
  * { margin: 0; padding: 0; box-sizing: border-box; }
  html, body {
    width: 1012px;
    height: 1200px;
    overflow: hidden;
    background: var(--paper);
    font-family: var(--serif);
  }
  .sheet { position: relative; width: 1012px; height: 1200px; }

  /* Front of card */
  .card-front {
    position: absolute;
    left: 0; top: 0;
    width: 1012px; height: 603px;
    background: var(--ink);
    color: var(--paper);
  }
  .front-name {
    position: absolute;
    left: 0; top: 150px;
    width: 1012px;
    text-align: center;
    font-weight: 700;
    line-height: 1.05;
  }
  .front-name .line-main { display: block; font-size: 120px; letter-spacing: -1px; }
  .front-name .line-trade { display: block; font-size: 104px; letter-spacing: 4px; }

  /* Back of card */
  .card-back {
    position: absolute;
    left: 0; top: 606px;
    width: 1012px; height: 594px;
    background: var(--paper);
  }
  .card-back .split { position: absolute; inset: 0; }

  .back-name {
    position: absolute;
    left: 330px; top: 370px;
    width: 640px;
    text-align: center;
    color: var(--paper);
    font-weight: 700;
    font-size: 54px;
    white-space: nowrap;
    transform: rotate(28.6deg);
    transform-origin: center;
  }

  .contact {
    position: absolute;
    left: 575px; top: 78px;
    width: 400px;
    text-align: center;
    color: var(--ink);
    font-size: 24px;
    line-height: 35px;
  }
  .contact .person { font-size: 28px; }

  .services {
    position: absolute;
    left: 70px; top: 298px;
    width: 300px;
    text-align: center;
    color: var(--paper);
    font-size: 28px;
    line-height: 40px;
  }
  .services .intro { margin-bottom: 10px; }
  .services ul { list-style: none; }
</style>
</head>
<body>
<main class="sheet">
  <section class="card-front">
    <h1 class="front-name">
      <span class="line-main">Bright Fern</span>
      <span class="line-trade">PAINTING</span>
    </h1>
  </section>

  <section class="card-back">
    <svg class="split" width="1012" height="594" viewBox="0 0 1012 594" aria-hidden="true">
      <polygon points="0,0 1012,553 1012,594 0,594" fill="var(--ink)"/>
    </svg>

    <div class="back-name">Bright Fern Painting</div>

    <address class="contact" style="font-style: normal;">
      <div class="person">Mark Hollis</div>
      <div>Quality Mangager</div>
      <div>Phone :555-014-2763</div>
      <div>Mark.BrightFern@fernmail.com</div>
      <div>BrightFernPainting.com</div>
    </address>

    <div class="services">
      <p class="intro">we do</p>
      <ul>
        <li>Exterior Painting</li>
        <li>Interior Painting</li>
        <li>Carpentry</li>
        <li>Drywall</li>
      </ul>
    </div>
  </section>
</main>
</body>
</html>
```